New locally owned rental company needs a flyer to circulate

Need flyer with logo, phone# and address. We rent cars to anyone with driver's license and proper insurance. Rates as low as $50/day. Can offer compact cars, mid-size and full size sedans. Also SUV's.

```html
<!DOCTYPE html>
<html lang="en">
<head>
<meta charset="utf-8">
<title>DriveSoon Car &amp; Van Rental Flyer</title>
<link rel="stylesheet" href="https://fonts.googleapis.com/css2?family=Anton&family=Poppins:wght@500;600;700;800&display=swap">
<style>
:root{
  --page:#dcdcdc;
  --navy:#0c2a5c;
  --blue:#1553b8;
  --blue-deep:#0e3f96;
  --green:#2db24f;
  --red:#e0141c;
  --ink:#1b1b1b;
  --footer:#1c1c1c;
  --white:#ffffff;
}
*{margin:0;padding:0;box-sizing:border-box}
html,body{width:1200px;height:2351px;overflow:hidden;background:var(--page)}
body{position:relative;font-family:"Poppins",sans-serif}
.flyer{position:absolute;left:50px;top:463px;width:1100px;height:1425px;background:var(--white);overflow:hidden;box-shadow:0 10px 30px rgba(0,0,0,.25)}
.abs{position:absolute}
.hero-bg{left:0;top:0;width:1100px;height:700px;background:linear-gradient(180deg,#1a4a9c 0%,#143f86 35%,var(--navy) 100%)}
.chevron{left:0;top:0}
.photo-people{left:655px;top:25px;width:420px;height:370px;border-radius:6px;background:radial-gradient(ellipse at 50% 40%,#9fb8dc 0%,#6f8fc4 55%,rgba(40,80,150,.6) 100%)}
.photo-car-hero{left:370px;top:325px;width:730px;height:330px;border-radius:40% 30% 20% 20%;background:radial-gradient(ellipse at 55% 55%,#d42230 0%,#a3121d 55%,rgba(160,30,40,.35) 100%)}
.brand{left:54px;top:50px;font-weight:800;font-size:60px;color:var(--white);line-height:1;letter-spacing:-1px}
.tagline{left:92px;top:120px;font-weight:700;font-size:26px;color:var(--white);letter-spacing:12px}
.headline{left:52px;top:200px;font-family:"Anton",sans-serif;font-size:124px;line-height:1.05;color:var(--white);letter-spacing:1px}
.headline .accent{color:var(--green)}
.intro{left:54px;top:342px;width:420px;font-weight:500;font-size:31px;line-height:40px;color:var(--white)}
.serving{left:54px;top:690px;font-weight:500;font-size:28px;line-height:40px;color:var(--ink)}
.serving strong{display:block;font-weight:700;font-size:31px;color:var(--blue)}
.feature{left:0;width:567px;height:72px;border-radius:0 14px 14px 0;display:flex;align-items:center;padding-left:56px;gap:12px;color:var(--white);font-weight:600;font-size:31px;box-shadow:4px 6px 8px rgba(0,0,0,.18)}
.feature svg{flex:none}
.feature.green{background:var(--green)}
.feature.blue{background:var(--blue)}
.rates{left:52px;top:1086px;font-weight:800;font-size:38px;line-height:40px;color:var(--ink)}
.price{left:262px;top:1064px;font-family:"Anton",sans-serif;font-size:96px;line-height:1.1;color:var(--red)}
.photo-car{border-radius:30% 30% 14% 14%}
.car-suv-grey{left:655px;top:680px;width:315px;height:180px;background:radial-gradient(ellipse at 50% 55%,#6b6e74 0%,#8d9096 60%,rgba(200,200,205,.4) 100%)}
.car-sedan-blue{left:655px;top:880px;width:320px;height:128px;background:radial-gradient(ellipse at 50% 55%,#1d3fb8 0%,#2e4fc9 60%,rgba(180,190,230,.4) 100%)}
.car-suv-silver{left:660px;top:1055px;width:305px;height:130px;background:radial-gradient(ellipse at 50% 55%,#9a9892 0%,#b8b6b0 60%,rgba(215,215,210,.4) 100%)}
.badge{width:116px;height:116px;border-radius:50%;background:var(--blue);display:flex;align-items:center;justify-content:center;box-shadow:0 0 0 0 var(--white)}
.badge::before{content:"";position:absolute;inset:7px;border:3px solid var(--white);border-radius:50%}
.badge span{color:var(--white);font-weight:700;font-size:23px;line-height:22px;text-align:center}
.cta-line{left:0;top:1257px;width:1100px;height:6px;background:var(--blue)}
.cta{left:0;top:1211px;width:1100px;height:50px}
.cta-text{left:0;top:1211px;width:1100px;text-align:center;font-weight:700;font-size:33px;line-height:50px;color:var(--white);padding-left:6px}
.footer{left:0;top:1263px;width:1100px;height:162px;background:var(--footer);color:var(--white)}
.call-label{left:73px;top:24px;font-weight:500;font-size:28px}
.phone{left:80px;top:58px;display:flex;align-items:center;gap:12px;font-weight:700;font-size:46px}
.address{left:500px;top:36px;display:flex;gap:14px;font-weight:500;font-size:30px;line-height:40px}
</style>
</head>
<body>
<main class="flyer">
  <div class="abs hero-bg"></div>
  <div class="abs photo-people" role="img" aria-label="Smiling couple holding car keys in front of rental office"></div>
  <div class="abs photo-car-hero" role="img" aria-label="Red compact sedan with rental windshield sign"></div>

  <svg class="abs chevron" width="1100" height="720" viewBox="0 0 1100 720" aria-hidden="true">
    <polygon points="0,540 225,625 1100,340 1100,380 225,660 0,578" fill="var(--green)"/>
    <polygon points="0,568 225,650 1100,372 1100,400 225,672 0,592" fill="var(--blue)"/>
    <polygon points="0,592 225,672 1100,400 1100,720 0,720" fill="var(--white)"/>
  </svg>

  <div class="abs brand">DriveSoon</div>
  <div class="abs tagline">Car &amp; Van Rental</div>
  <h1 class="abs headline">RENT <span class="accent">A CAR</span></h1>
  <p class="abs intro">We rent cars to anyone with driver's license and proper insurance</p>

  <p class="abs serving">Car and van rental company serving <strong>Huntsville, AL. metropolitan area</strong></p>

  <div class="abs feature green" style="top:792px">
    <svg width="22" height="22" viewBox="0 0 22 22"><circle cx="11" cy="11" r="11" fill="#fff"/><path d="M6 11.5l3.2 3L16 7.8" stroke="var(--green)" stroke-width="2.6" fill="none" stroke-linecap="round" stroke-linejoin="round"/></svg>
    We offer compact cars
  </div>
  <div class="abs feature blue" style="top:884px">
    <svg width="22" height="22" viewBox="0 0 22 22"><circle cx="11" cy="11" r="11" fill="#fff"/><path d="M6 11.5l3.2 3L16 7.8" stroke="var(--blue)" stroke-width="2.6" fill="none" stroke-linecap="round" stroke-linejoin="round"/></svg>
    Mid-size and full size sedans
  </div>
  <div class="abs feature green" style="top:977px">
    <svg width="22" height="22" viewBox="0 0 22 22"><circle cx="11" cy="11" r="11" fill="#fff"/><path d="M6 11.5l3.2 3L16 7.8" stroke="var(--green)" stroke-width="2.6" fill="none" stroke-linecap="round" stroke-linejoin="round"/></svg>
    SUV's also available
  </div>

  <p class="abs rates">RATES AS<br>LOW AS</p>
  <p class="abs price">$50/DAY</p>

  <div class="abs photo-car car-suv-grey" role="img" aria-label="Grey mid-size SUV"></div>
  <div class="abs photo-car car-sedan-blue" role="img" aria-label="Blue full size sedan"></div>
  <div class="abs photo-car car-suv-silver" role="img" aria-label="Silver compact SUV"></div>

  <div class="abs badge" style="left:924px;top:606px"><span>RENT<br>NOW</span></div>
  <div class="abs badge" style="left:931px;top:817px"><span>RENT<br>NOW</span></div>
  <div class="abs badge" style="left:921px;top:1002px"><span>RENT<br>NOW</span></div>

  <svg class="abs cta" width="1100" height="50" viewBox="0 0 1100 50" aria-hidden="true">
    <polygon points="198,0 902,0 922,50 178,50" fill="var(--blue)"/>
  </svg>
  <div class="abs cta-line"></div>
  <p class="abs cta-text">BOOK YOUR FAVOURITE CAR TODAY</p>

  <footer class="abs footer">
    <p class="abs call-label">CALL NOW</p>
    <p class="abs phone">
      <svg width="40" height="40" viewBox="0 0 24 24" aria-hidden="true"><path d="M6.6 10.8a15.1 15.1 0 006.6 6.6l2.2-2.2a1 1 0 011-.25 11.4 11.4 0 003.6.57 1 1 0 011 1V20a1 1 0 01-1 1A17 17 0 013 4a1 1 0 011-1h3.5a1 1 0 011 1c0 1.25.2 2.45.57 3.6a1 1 0 01-.25 1z" fill="var(--green)"/></svg>
      256-555-0147
    </p>
    <div class="abs address">
      <svg width="30" height="40" viewBox="0 0 24 32" aria-hidden="true"><path d="M12 1a9 9 0 00-9 9c0 6.8 9 17 9 17s9-10.2 9-17a9 9 0 00-9-9z" fill="none" stroke="var(--green)" stroke-width="3"/><circle cx="12" cy="10" r="3.4" fill="var(--green)"/><rect x="4" y="29" width="16" height="2.6" rx="1.3" fill="var(--green)"/></svg>
      <p>4800 Cedar Ridge Boulevard<br>Huntsville, AL 35801</p>
    </div>
  </footer>
</main>
</body>
</html>
```